Referral Portal - Mobile App Design

To create a clean easy Web App Design for a Referral portal for Customer to submit and track their referrals.

Larkmoor Energy Referral Portal

https://www.larkmoor-energy.example

We are looking for a very simple phone app that will allow users to track their referrals. The sections/ things
We need in the app are as follows:
Form to Submit new Referrals
A very visual easy to read dashboard/ graph to show total Paid vs total potential(outstanding)
Simple Visual to show total paid
List of all referrals submitted and their status
Total number of referrals submitted and what Tier they fall into and what is the next tier (how close)

The App should be a minimal clean design that the user can navigate easily without much direction given.
This app should only be designed for the mobile experience. This is meant to gamify and incentives the user
To add more referrals and get more payments. Adding something fun with the Sun would be great!

Please See Bridge file for further information. We would like to name the App Larkmoor Energy Bridge

Thank you!!

Target Market(s)

Homeowners between ages of 30-60 who are familiar with apps that they use on their phone every day

Industry/Entity Type

Solar Energy

Font styles to use
Sans Serif

Colors
fbee3e
acd136
9bcb3c
f68e4e
f37022
f78f20
ffc214
34a7d8

Requirements
Must have
• Clean simple design, easy to use design/layout of nav.
• Visual charts and big graphic $$ on how much they have in their Wallet
• Easy visual to tell apart tiers (Gold, Silver,Platinum)
Nice to have
• Fun way to incorporate a rising or glowing sun
Should not have
• Too many words, not be bright and color

```html
<!DOCTYPE html>
<html lang="en">
<head>
<meta charset="utf-8">
<title>Larkmoor Energy Bridge – Stats</title>
<link rel="stylesheet" href="https://fonts.googleapis.com/css2?family=Roboto:wght@300;400&display=swap">
<style>
  :root {
    --orange: #f8924c;
    --orange-deep: #e07f3f;
    --orange-text: #f68e4e;
    --dot: #f0814a;
    --sun-yellow: #fde92a;
    --warm-peach: #ff8c5e;
    --axis: #b5b5b5;
    --white: #ffffff;
  }
  * { box-sizing: border-box; margin: 0; padding: 0; }
  html, body { width: 676px; height: 1200px; overflow: hidden; background: var(--white); }
  body { font-family: "Roboto", sans-serif; font-weight: 300; position: relative; }

  .status-bar {
    position: absolute; top: 0; left: 0; width: 676px; height: 40px;
    background: var(--orange-deep); color: var(--white);
    font-size: 19px; font-weight: 400;
  }
  .status-bar .time { position: absolute; left: 0; right: 0; top: 9px; text-align: center; }
  .status-bar .signal { position: absolute; left: 17px; top: 12px; }
  .status-bar .battery-level { position: absolute; right: 72px; top: 9px; }
  .status-bar .battery { position: absolute; right: 18px; top: 11px; }

  .app-header {
    position: absolute; top: 40px; left: 0; width: 676px; height: 88px;
    background: var(--orange); color: var(--white);
  }
  .app-header .menu-button { position: absolute; left: 30px; top: 37px; }
  .app-header .screen-title {
    position: absolute; left: 0; right: 0; top: 30px; text-align: center;
    font-size: 30px; font-weight: 300;
  }

  .tier-name {
    position: absolute; top: 132px; left: 0; right: 0; text-align: center;
    font-size: 72px; font-weight: 300; color: var(--orange-text); letter-spacing: 1px;
  }
  .earning-row {
    position: absolute; top: 229px; left: 0; width: 676px; height: 62px;
  }
  .earning-label {
    position: absolute; left: 101px; top: 12px;
    font-size: 31px; font-weight: 300; color: var(--orange-text);
  }
  .earning-amount {
    position: absolute; left: 411px; top: 0; width: 177px; height: 61px;
    border-radius: 31px; background: var(--orange); color: var(--white);
    font-size: 31px; font-weight: 300; text-align: center; line-height: 61px;
  }

  .earnings-chart { position: absolute; left: 0; top: 359px; }
  .earnings-chart .axis-label { font-family: "Roboto", sans-serif; font-weight: 300; font-size: 24px; fill: var(--white); }
  .earnings-chart .tooltip-text { font-family: "Roboto", sans-serif; font-weight: 300; font-size: 16px; fill: var(--white); }

  .refer-button {
    position: absolute; left: 0; top: 1100px; width: 676px; height: 100px;
    background: var(--orange); color: var(--white); border: none;
    font-family: "Roboto", sans-serif; font-weight: 300; font-size: 30px;
    letter-spacing: 0.5px; text-align: center; line-height: 100px;
  }
</style>
</head>
<body>
  <div class="status-bar">
    <svg class="signal" width="110" height="18" viewBox="0 0 110 18" aria-hidden="true">
      <circle cx="7" cy="8" r="6" fill="#fff"/>
      <circle cx="22" cy="8" r="6" fill="#fff"/>
      <circle cx="37" cy="8" r="6" fill="#fff"/>
      <circle cx="52" cy="8" r="5.3" fill="none" stroke="#fff" stroke-width="1.3"/>
      <circle cx="67" cy="8" r="5.3" fill="none" stroke="#fff" stroke-width="1.3"/>
      <path d="M82 5 a17 17 0 0 1 22 0" fill="none" stroke="#fff" stroke-width="2.4"/>
      <path d="M86 9 a11 11 0 0 1 14 0" fill="none" stroke="#fff" stroke-width="2.4"/>
      <path d="M90 13 l3 3 l3 -3 a5 5 0 0 0 -6 0z" fill="#fff"/>
    </svg>
    <span class="time">08:46 PM</span>
    <span class="battery-level">57%</span>
    <svg class="battery" width="50" height="20" viewBox="0 0 50 20" aria-hidden="true">
      <rect x="1" y="1" width="44" height="18" rx="4" fill="none" stroke="#fff" stroke-width="1.6"/>
      <rect x="4" y="4" width="22" height="12" rx="2" fill="#fff"/>
      <rect x="46" y="7" width="3" height="6" rx="1" fill="#fff"/>
    </svg>
  </div>

  <header class="app-header">
    <svg class="menu-button" width="44" height="24" viewBox="0 0 44 24" aria-label="Menu" role="img">
      <rect x="0" y="0" width="44" height="4" rx="2" fill="#fff"/>
      <rect x="0" y="10" width="44" height="4" rx="2" fill="#fff"/>
      <rect x="0" y="20" width="44" height="4" rx="2" fill="#fff"/>
    </svg>
    <h1 class="screen-title">Stats</h1>
  </header>

  <main>
    <div class="tier-name">SILVER</div>
    <div class="earning-row">
      <span class="earning-label">Your Total Earning :</span>
      <span class="earning-amount">500$</span>
    </div>

    <svg class="earnings-chart" width="676" height="571" viewBox="0 340 640 540" role="img" aria-label="Referral earnings over time">
      <defs>
        <linearGradient id="area-fill" x1="0" y1="520" x2="0" y2="856" gradientUnits="userSpaceOnUse">
          <stop offset="0" stop-color="var(--sun-yellow)"/>
          <stop offset="1" stop-color="var(--warm-peach)"/>
        </linearGradient>
      </defs>
      <polygon points="60,856 189,676 268,710 400,628 452,628 545,520 619,735 619,856" fill="url(#area-fill)"/>
      <line x1="60" y1="856" x2="60" y2="366" stroke="var(--axis)" stroke-width="2"/>
      <polygon points="52,372 60,357 68,372" fill="var(--axis)"/>
      <line x1="60" y1="856" x2="596" y2="856" stroke="var(--axis)" stroke-width="2"/>
      <polygon points="590,850 605,856 590,862" fill="var(--axis)"/>

      <g fill="var(--dot)">
        <circle cx="189" cy="676" r="6"/>
        <circle cx="268" cy="710" r="6"/>
        <circle cx="400" cy="628" r="6"/>
        <circle cx="452" cy="628" r="6"/>
        <circle cx="545" cy="520" r="6"/>
        <circle cx="619" cy="735" r="6"/>
      </g>

      <g class="tooltip">
        <rect x="109" y="608" width="159" height="42" rx="21" fill="var(--orange)"/>
        <polygon points="177,649 185,666 193,649" fill="var(--orange)"/>
        <text class="tooltip-text" x="188.5" y="636" text-anchor="middle">12 September</text>
      </g>

      <g class="y-axis-labels">
        <circle cx="28" cy="405" r="21" fill="var(--orange)"/>
        <text class="axis-label" x="28" y="414" text-anchor="middle">4</text>
        <circle cx="28" cy="517" r="21" fill="var(--orange)"/>
        <text class="axis-label" x="28" y="526" text-anchor="middle">3</text>
        <circle cx="28" cy="628" r="21" fill="var(--orange)"/>
        <text class="axis-label" x="28" y="637" text-anchor="middle">2</text>
        <circle cx="28" cy="740" r="21" fill="var(--orange)"/>
        <text class="axis-label" x="28" y="749" text-anchor="middle">1</text>
        <circle cx="28" cy="853" r="21" fill="var(--orange)"/>
        <text class="axis-label" x="28" y="862" text-anchor="middle">0</text>
      </g>
    </svg>
  </main>

  <button class="refer-button" type="button">REFER NEW FRIEND</button>
</body>
</html>
```